Shipping container company needs 7 print ads developed

We sell and rent shipping containers as affordable storage solutions.Target markets are agricultural, construction, commercial, warehouse, manufacturing, and hobby farms. I need seven persona -specific (see attached 7 personas) clean minimalistic 4.375" x 4" ads in color with graphics, copy, 20' stock container image, and logo. Also, see attached brand guidelines.. Special note -phone number needs to be changed to 555.014.3829

```html
<!DOCTYPE html>
<html lang="en">
<head>
<meta charset="utf-8">
<title>Portable Storage for Every Job Site</title>
<link rel="stylesheet" href="https://fonts.googleapis.com/css2?family=Outfit:wght@300;400;600;700&display=swap">
<style>
  :root {
    --navy: #0f1c2e;
    --navy-deep: #0c1a2b;
    --teal: #1a9e8c;
    --paper: #ebebea;
    --white: #ffffff;
    --steel-dark: #1a2c4e;
    --steel-light: #3b5788;
  }
  * { margin: 0; padding: 0; box-sizing: border-box; }
  html, body { width: 1200px; height: 1096px; overflow: hidden; }
  body { font-family: "Outfit", sans-serif; color: var(--navy); }
  .ad {
    position: relative; width: 1200px; height: 1096px; overflow: hidden;
    background: radial-gradient(ellipse at 40% 30%, #f5f5f4 0%, var(--paper) 70%, #dcdcda 100%);
  }
  .footer-band {
    position: absolute; left: 0; top: 685px; width: 1200px; height: 411px;
    background: var(--navy-deep);
  }
  .feature-icons { position: absolute; left: 68px; top: 80px; display: flex; gap: 26px; }
  .feature-icon {
    width: 70px; height: 70px; border: 3px solid var(--teal); border-radius: 50%;
    display: flex; align-items: center; justify-content: center;
  }
  .headline {
    position: absolute; left: 70px; top: 186px;
    font-size: 69px; font-weight: 600; line-height: 84px; letter-spacing: -0.5px;
  }
  .headline .circled { position: relative; display: inline-block; }
  .headline .circled svg { position: absolute; left: -10px; top: -8px; }
  .headline .underlined { position: relative; display: inline-block; }
  .headline .underlined svg { position: absolute; left: -2px; bottom: -6px; }
  .headline .dot { color: var(--teal); }
  .intro {
    position: absolute; left: 70px; top: 382px;
    font-size: 33px; font-weight: 400; line-height: 46px;
  }
  .teal { color: var(--teal); }
  .rule { position: absolute; height: 3px; }
  .rule-intro { left: 70px; top: 605px; width: 68px; background: var(--teal); }
  .brand {
    position: absolute; right: 70px; top: 92px;
    display: flex; align-items: center; gap: 14px;
  }
  .brand-mark { width: 40px; height: 40px; background: var(--navy); }
  .brand-name { font-size: 34px; font-weight: 600; color: var(--navy); line-height: 1; }
  .tagline {
    position: absolute; right: 70px; top: 212px; text-align: right;
    font-size: 34px; line-height: 42px; font-weight: 400;
  }
  .tagline strong { color: var(--teal); font-weight: 600; }
  .rule-tagline { right: 70px; top: 319px; width: 68px; background: var(--navy); }
  .container-photo {
    position: absolute; left: 620px; top: 410px; width: 580px; height: 686px;
    background: linear-gradient(100deg, var(--steel-dark) 0%, var(--steel-light) 45%, #27406b 75%, var(--steel-dark) 100%);
    clip-path: polygon(12% 14%, 48% 8%, 100% 4%, 100% 100%, 50% 100%, 13% 94%);
  }
  .cta-button {
    position: absolute; left: 68px; top: 751px; width: 275px; height: 68px;
    background: var(--teal); border-radius: 8px; color: var(--white);
    font-size: 33px; font-weight: 600; display: flex; align-items: center; justify-content: center;
  }
  .cta-text {
    position: absolute; left: 68px; top: 840px; color: var(--white);
    font-size: 35px; font-weight: 300; line-height: 46px;
  }
  .cta-text .teal { font-weight: 400; }
  .phone {
    position: absolute; left: 68px; top: 958px; width: 347px; height: 69px;
    border: 2px solid var(--teal); border-radius: 8px;
    display: flex; align-items: center; gap: 18px; padding-left: 18px;
    color: var(--white); font-size: 40px; font-weight: 600;
  }
</style>
</head>
<body>
<div class="ad">
  <div class="footer-band"></div>

  <div class="feature-icons">
    <div class="feature-icon">
      <svg width="36" height="36" viewBox="0 0 24 24" fill="none" stroke="#0f1c2e" stroke-width="2" stroke-linejoin="round" stroke-linecap="round"><path d="M12 2l8 3v6c0 5-3.5 9-8 11-4.5-2-8-6-8-11V5z"/><path d="M8.5 12l2.5 2.5 4.5-5"/></svg>
    </div>
    <div class="feature-icon">
      <svg width="38" height="38" viewBox="0 0 24 24" fill="none" stroke="#0f1c2e" stroke-width="2" stroke-linejoin="round"><path d="M3 8l9-4 9 4v8l-9 4-9-4z"/><path d="M3 8l9 4 9-4M12 12v8M15 10.5v8M18 9.2v8"/></svg>
    </div>
    <div class="feature-icon">
      <svg width="38" height="38" viewBox="0 0 24 24" fill="none" stroke="#0f1c2e" stroke-width="2" stroke-linejoin="round"><path d="M2 6h12v10H2zM14 9h4l4 4v3h-8z"/><circle cx="6" cy="17.5" r="2" fill="#ebebea"/><circle cx="17" cy="17.5" r="2" fill="#ebebea"/></svg>
    </div>
  </div>

  <h1 class="headline">
    <span class="circled">Portable<svg width="320" height="100" viewBox="0 0 320 100" fill="none"><ellipse cx="160" cy="50" rx="155" ry="42" stroke="#1a9e8c" stroke-width="5" transform="rotate(-3 160 50)"/></svg></span> Storage<br>
    for Every <span class="underlined">Job Site<svg width="300" height="12" viewBox="0 0 300 12" fill="none"><path d="M2 7 Q150 2 298 6" stroke="#1a9e8c" stroke-width="5" stroke-linecap="round"/></svg></span><span class="dot">.</span>
  </h1>

  <p class="intro">
    <span class="teal">Durable containers</span><br>
    designed to secure tools,<br>
    materials, and more<span class="teal">.</span><br>
    <span class="teal">Right where you need them.</span>
  </p>
  <div class="rule rule-intro"></div>

  <div class="brand">
    <div class="brand-mark"></div>
    <div class="brand-name">Ridgeline Containers</div>
  </div>
  <p class="tagline">Trusted containers,<br><strong>exceptional service.</strong></p>
  <div class="rule rule-tagline"></div>

  <div class="container-photo" role="img" aria-label="Navy blue 20-foot steel shipping container with closed cargo doors, seen from a low front angle"></div>

  <div class="cta-button">Contact Us</div>
  <p class="cta-text">Get <span class="teal">personalized solutions</span><br>for your needs.</p>
  <div class="phone">
    <svg width="34" height="34" viewBox="0 0 24 24" fill="none" stroke="#1a9e8c" stroke-width="2" stroke-linejoin="round"><path d="M5 3h4l2 5-2.5 1.5a11 11 0 005 5L15 12l5 2v4a2 2 0 01-2 2A16 16 0 013 5a2 2 0 012-2z"/></svg>
    <span>555.014.3829</span>
  </div>
</div>
</body>
</html>
```